Simple, elegant, business card design required

Hi designers,I am looking for a simple yet elegant business card design.

Please make use of my logo (attached); you are free to tweak the logo should you wish to do so.

Our business is involved in many different fields - almost all of them involved in some form of "design", so that's really one of the key things I want to portray. I do not wish to specify which field of design, exactly.

I prefer white on black (or just monochromatic), but if you have a different, creative idea, I am open to that too.

You can use artsy photographs provided that you have the license to use those. Please feel free to ask me any questions.

Target Market(s)

High-end customers looking for design consultancy

Industry/Entity Type

Business

Contact Information for Business Card

Name: Gareth Pellwinter
Position: Creative Director
Mobile: +150963218745
Address: Morrow Lane, Stratford upon Avon, Warwickshire CV37 2JT
Website: corvastudio.com (not launched yet)

Requirements
Must have
• Design layout must be clean, original, and text must be readable when printed.
Should not have
• ~ No business card templates please. Anyone using this will be reported.
• ~ Please don't spam entries.

```html
<!DOCTYPE html>
<html lang="en">
<head>
<meta charset="utf-8">
<title>Corvastudio business card</title>
<link rel="stylesheet" href="https://fonts.googleapis.com/css2?family=Josefin+Sans:wght@400&family=Oswald:wght@500&family=Exo+2:wght@400&display=swap">
<style>
  :root {
    --backdrop: #e9e5df;
    --paper: #ffffff;
    --ink: #1e1e1e;
    --charcoal: #2a2a2a;
    --gold-light: #eadfc6;
    --gold-dark: #b9a57c;
    --muted: #444444;
  }
  * { box-sizing: border-box; margin: 0; padding: 0; }
  html, body {
    width: 1200px; height: 987px; overflow: hidden;
    background: var(--backdrop);
  }
  .stage { position: relative; width: 1200px; height: 987px; }
  .card {
    position: absolute; top: 143px; width: 400px; height: 700px;
    background: var(--paper);
    box-shadow: 0 18px 40px rgba(0,0,0,0.18);
    overflow: hidden;
  }
  .card--back { left: 150px; }
  .card--front { left: 650px; }
  .card__shapes { position: absolute; inset: 0; }
  .brand {
    position: absolute; left: 0; right: 0;
    display: flex; flex-direction: column; align-items: center; gap: 22px;
  }
  .brand__mark {
    width: 30px; height: 30px; border: 3px solid var(--ink); border-radius: 50%;
  }
  .brand__name {
    font-family: "Josefin Sans", sans-serif; font-weight: 400;
    font-size: 27px; letter-spacing: 9px; color: var(--ink);
    padding-left: 9px;
  }
  .card--back .brand { top: 245px; }
  .card--front .brand { top: 140px; }
  .person {
    position: absolute; top: 272px; right: 60px; text-align: center;
  }
  .person__name {
    font-family: "Oswald", sans-serif; font-weight: 500;
    font-size: 30px; letter-spacing: 1px; color: var(--ink); line-height: 1.1;
  }
  .person__role {
    font-family: "Exo 2", sans-serif; font-size: 15px; letter-spacing: 1.5px;
    color: var(--ink); text-transform: uppercase;
  }
  .contacts {
    position: absolute; top: 360px; left: 30px; right: 24px;
    display: grid; grid-template-columns: 1fr 1.25fr; row-gap: 12px; column-gap: 10px;
    font-family: "Exo 2", sans-serif; font-size: 11.5px; color: var(--muted);
  }
  .contact { display: flex; align-items: center; gap: 6px; white-space: nowrap; }
  .contact svg { width: 15px; height: 15px; flex: none; }
  .location {
    position: absolute; top: 558px; left: 0; right: 0;
    display: flex; flex-direction: column; align-items: center; gap: 12px;
  }
  .location svg { width: 34px; height: 34px; }
  .location__address {
    font-family: "Exo 2", sans-serif; font-size: 13px; line-height: 1.55;
    color: #f2f2f2; text-align: center; letter-spacing: 0.5px;
  }
</style>
</head>
<body>
<main class="stage">

  <section class="card card--back" aria-label="Card back">
    <svg class="card__shapes" viewBox="0 0 400 700" aria-hidden="true">
      <defs>
        <linearGradient id="goldBack" x1="0" y1="0" x2="1" y2="0">
          <stop offset="0" stop-color="var(--gold-dark)"/>
          <stop offset="0.5" stop-color="var(--gold-light)"/>
          <stop offset="1" stop-color="var(--gold-dark)"/>
        </linearGradient>
      </defs>
      <polygon points="0,0 400,0 400,34 200,8 0,34" fill="url(#goldBack)"/>
      <polygon points="0,460 200,530 400,460 400,700 0,700" fill="url(#goldBack)"/>
      <polygon points="0,474 200,544 400,474 400,700 0,700" fill="var(--charcoal)"/>
    </svg>
    <div class="brand">
      <span class="brand__mark"></span>
      <span class="brand__name">CORVASTUDIO</span>
    </div>
  </section>

  <section class="card card--front" aria-label="Card front">
    <svg class="card__shapes" viewBox="0 0 400 700" aria-hidden="true">
      <defs>
        <linearGradient id="goldFront" x1="0" y1="0" x2="1" y2="0">
          <stop offset="0" stop-color="var(--gold-dark)"/>
          <stop offset="0.5" stop-color="var(--gold-light)"/>
          <stop offset="1" stop-color="var(--gold-dark)"/>
        </linearGradient>
      </defs>
      <polygon points="0,0 400,0 400,34 200,8 0,34" fill="url(#goldFront)"/>
      <polygon points="0,460 200,530 400,460 400,700 0,700" fill="url(#goldFront)"/>
      <polygon points="0,474 200,544 400,474 400,700 0,700" fill="var(--charcoal)"/>
    </svg>

    <div class="brand">
      <span class="brand__mark"></span>
      <span class="brand__name">CORVASTUDIO</span>
    </div>

    <div class="person">
      <p class="person__name">GARETH PELLWINTER</p>
      <p class="person__role">General Manager</p>
    </div>

    <div class="contacts">
      <p class="contact">
        <svg viewBox="0 0 16 16" aria-hidden="true"><circle cx="8" cy="8" r="7" fill="none" stroke="#444" stroke-width="1.2"/><path d="M5.5 4.5l1.5 0 .6 2-1 .8a5 5 0 0 0 2 2l.8-1 2 .6 0 1.5c-3.5.4-6.3-2.4-5.9-5.9z" fill="#444"/></svg>
        +150963218745
      </p>
      <p class="contact">
        <svg viewBox="0 0 16 16" aria-hidden="true"><circle cx="8" cy="8" r="7" fill="none" stroke="#444" stroke-width="1.2"/><rect x="4.5" y="5" width="7" height="6" rx="0.8" fill="none" stroke="#444" stroke-width="1.1"/><path d="M4.5 5.5l3.5 2.8 3.5-2.8" fill="none" stroke="#444" stroke-width="1.1"/></svg>
        hello@corvastudio.com
      </p>
      <p class="contact">
        <svg viewBox="0 0 16 16" aria-hidden="true"><circle cx="8" cy="8" r="7" fill="none" stroke="#444" stroke-width="1.2"/><path d="M5.5 4.5l1.5 0 .6 2-1 .8a5 5 0 0 0 2 2l.8-1 2 .6 0 1.5c-3.5.4-6.3-2.4-5.9-5.9z" fill="#444"/></svg>
        +150963218745
      </p>
      <p class="contact">
        <svg viewBox="0 0 16 16" aria-hidden="true"><circle cx="8" cy="8" r="7" fill="none" stroke="#444" stroke-width="1.2"/><circle cx="8" cy="8" r="3.8" fill="none" stroke="#444" stroke-width="1"/><path d="M4.2 8h7.6M8 4.2v7.6" stroke="#444" stroke-width="1"/></svg>
        www.corvastudio.com
      </p>
    </div>

    <div class="location">
      <svg viewBox="0 0 34 34" aria-hidden="true"><circle cx="17" cy="17" r="16" fill="#f2f2f2"/><path d="M17 8a6 6 0 0 0-6 6c0 4.5 6 11 6 11s6-6.5 6-11a6 6 0 0 0-6-6z" fill="var(--charcoal)"/><circle cx="17" cy="14" r="2.2" fill="#f2f2f2"/></svg>
      <p class="location__address">Morrow Lane, Stratford upon Avon,<br>Warwickshire CV37 2JT</p>
    </div>
  </section>

</main>
</body>
</html>
```